Website Design for Horse Blog
Purely Brivelle
Project: Website Design for Horse Blog
Website Design for Horse Blog - Blogging
Creative Brief
Blogging
Brivelle Saddlebreds is a boutique saddlebred horse breeding operation. Purely Brivelle is the name of the blog encouraging older people that it is never too late to start riding horses. It's a feel-good blog intended to attract more people to the Saddlebred Horse Showing industry.
Simple, user-friendly without too much going on. Photography is important.
Modern
Burgundy
Black
Ivory
left side
http://joannevrelstad.example
Most importantly I want to set this website for blogging purposes. The business is just an example of what it is I do. Links to resources will be important for a page. I'm thinking five pages: Blog/Brivelle Saddlebreds/For Sale/Links/Contact Info
crewdalvo crewdalvo
Here is my revised requests: Five pages should be: Home, Blog, Brivelle Saddlebreds, Contact, Links. The title: Purely Brivelle should appear on the Home page along with the Brivelle Saddlebreds logo. I like simple, modern looking pages without a lot of information hitting me from every direction. I have seen very few with black backgrounds, I would like to see more of that.
I think I would like to see the title Purely Brivelle to be displayed with more emphasis as soon as the page loads.

```html
<!DOCTYPE html>
<html lang="en">
<head>
<meta charset="utf-8">
<title>Purely Brivelle</title>
<link href="https://fonts.googleapis.com/css2?family=Open+Sans:ital,wght@0,300;0,400;0,700;1,400&display=swap" rel="stylesheet">
<style>
  :root {
    --page-bg: #efebe4;
    --card-bg: #ffffff;
    --burgundy: #7c1212;
    --burgundy-deep: #5e0c0c;
    --ivory: #fbf6ec;
    --gold: #f2d27a;
    --ink: #2a2a2a;
    --muted: #7d7d7d;
    --rule: #e6e2db;
  }
  * { box-sizing: border-box; margin: 0; padding: 0; }
  html, body { width: 1200px; height: 1018px; overflow: hidden; }
  body {
    background: var(--page-bg);
    font-family: "Open Sans", Arial, sans-serif;
    color: var(--ink);
    position: relative;
  }
  .site {
    position: absolute;
    left: 99px; top: 61px;
    width: 1002px; height: 891px;
    background: var(--card-bg);
    box-shadow: 0 2px 10px rgba(0,0,0,0.08);
  }
  .masthead {
    height: 176px;
    text-align: center;
    padding-top: 44px;
  }
  .brand-name {
    font-weight: 300;
    font-size: 44px;
    letter-spacing: 1px;
    color: var(--ink);
    line-height: 1;
  }
  .brand-tagline {
    margin-top: 14px;
    font-size: 14px;
    letter-spacing: 6px;
    color: #555;
  }
  .hero {
    display: flex;
    height: 600px;
  }
  .sidebar {
    width: 355px;
    background: var(--burgundy);
    background-image: linear-gradient(160deg, var(--burgundy) 0%, var(--burgundy-deep) 100%);
    color: var(--ivory);
    padding: 34px 0 0 38px;
    position: relative;
  }
  .main-nav ul { list-style: none; }
  .main-nav li {
    display: flex; align-items: center;
    height: 44px;
    font-weight: 700;
    font-size: 14px;
    text-transform: uppercase;
  }
  .main-nav li.is-current { color: var(--gold); }
  .main-nav svg { width: 20px; height: 20px; margin-right: 12px; fill: currentColor; }
  .social {
    display: flex; gap: 10px;
    margin-top: 28px;
  }
  .social span {
    width: 34px; height: 34px;
    border: 2px solid var(--ivory);
    border-radius: 50%;
  }
  .welcome {
    position: absolute;
    left: 38px; top: 392px; right: 36px;
  }
  .welcome-kicker { font-size: 17px; font-weight: 400; text-transform: uppercase; }
  .welcome-title { font-size: 21px; font-weight: 700; text-transform: uppercase; line-height: 1.1; }
  .welcome-text {
    margin-top: 14px;
    font-size: 13px; font-style: italic; line-height: 1.55;
  }
  .read-more {
    display: block; margin-top: 20px;
    font-size: 13px; font-weight: 700; text-transform: uppercase;
    color: var(--ivory); text-decoration: none;
  }
  .hero-photo {
    flex: 1;
    position: relative;
    background: linear-gradient(180deg, #dfe3e6 0%, #c9cdcc 45%, #7a5a3e 62%, #6f8a4c 78%, #587a3a 100%);
  }
  .slide-dots {
    position: absolute; right: 56px; bottom: 34px;
    display: flex; gap: 8px;
  }
  .slide-dots span { width: 24px; height: 3px; background: rgba(255,255,255,0.6); }
  .slide-dots span.is-active { background: var(--burgundy); }
  .site-footer {
    text-align: center;
    padding-top: 42px;
    font-size: 12px;
    color: var(--muted);
    line-height: 2;
  }
</style>
</head>
<body>
  <div class="site">
    <header class="masthead">
      <div class="brand-name">Brivelle Saddlebreds</div>
      <div class="brand-tagline">PURELY BRIVELLE</div>
    </header>

    <section class="hero">
      <aside class="sidebar">
        <nav class="main-nav">
          <ul>
            <li class="is-current"><svg viewBox="0 0 20 20"><path d="M10 2 1 10h3v8h4v-5h4v5h4v-8h3z"/></svg>Home</li>
            <li><svg viewBox="0 0 20 20"><path d="M10 2C5 2 1 5 1 9c0 2 1 4 3 5l-1 4 4-3c1 0 2 .3 3 .3 5 0 9-3 9-7s-4-6.3-9-6.3z"/></svg>Blog</li>
            <li><svg viewBox="0 0 20 20"><circle cx="10" cy="10" r="8"/><rect x="9" y="8" width="2" height="7" fill="#7c1212"/><circle cx="10" cy="5.5" r="1.2" fill="#7c1212"/></svg>Brivelle Saddlebreds</li>
            <li><svg viewBox="0 0 20 20"><path d="M2 2h7l9 9-7 7-9-9z"/><circle cx="5.5" cy="5.5" r="1.5" fill="#7c1212"/></svg>For Sale</li>
            <li><svg viewBox="0 0 20 20"><path d="M8 12l4-4M6 9l-3 3a3 3 0 0 0 4 4l3-3M14 11l3-3a3 3 0 0 0-4-4l-3 3" stroke="currentColor" stroke-width="2.2" fill="none" stroke-linecap="round"/></svg>Links</li>
            <li><svg viewBox="0 0 20 20"><path d="M4 2l3 0 2 4-2 2c1 2 3 4 5 5l2-2 4 2v3c0 1-1 2-2 2C9 18 2 11 2 4c0-1 1-2 2-2z"/></svg>Contact</li>
          </ul>
        </nav>
        <div class="social" aria-label="Social links">
          <span></span><span></span><span></span><span></span>
        </div>

        <div class="welcome">
          <div class="welcome-kicker">Welcome to</div>
          <div class="welcome-title">Brivelle Saddlebreds</div>
          <p class="welcome-text">Purely Brivelle is the name of the blog encouraging older people that it is never too late to start riding horses.</p>
          <a class="read-more" href="#">Read more &gt;&gt;</a>
        </div>
      </aside>

      <div class="hero-photo" role="img" aria-label="Photo of a rider in black standing between two chestnut Saddlebred horses beside a dark wooden fence on green grass">
        <div class="slide-dots"><span class="is-active"></span><span></span><span></span></div>
      </div>
    </section>

    <footer class="site-footer">
      <div>130 Harlow Street No. 240 &nbsp;|&nbsp; 1 555 010 2040 &nbsp;|&nbsp; info@brivellesaddlebreds.example</div>
      <div>Copyright © 2015 Brivelle Saddlebreds. All Rights Reserved.</div>
    </footer>
  </div>
</body>
</html>
```